5Marble Strategy- Logo & Design Work

THIS IS PHASE ONE. I have a stock trading strategy. I need a schematic that shows how it works. I have included sketches. I want the scheme to look like Exhibit A. I want the circles to look like gear shifts in Exhibit B. After this first step is done, we will move on to creating logo like Exhibit C, a second logo like Exhibit D and another Schematic like Exhibit E.

```html
<!DOCTYPE html>
<html lang="en">
<head>
<meta charset="utf-8">
<title>5Marble Strategy – Exhibits</title>
<link rel="stylesheet" href="https://fonts.googleapis.com/css2?family=Poppins:wght@400;500;600;700;800&family=Oswald:wght@600&display=swap">
<style>
  :root {
    --stage: #000000;
    --paper: #ffffff;
    --navy: #1f2a6b;
    --navy-deep: #151d55;
    --blue: #2a3d8f;
    --red: #e0202e;
    --red-deep: #a8141f;
    --green: #1f9a3e;
    --green-deep: #137a2c;
    --tab-dark: #2b2b2b;
    --tab-light: #9a9a9a;
    --steel: #8e8e8e;
    --steel-light: #d9d9d9;
    --ink: #222222;
    --placeholder: #e6e6e6;
  }
  * { box-sizing: border-box; margin: 0; padding: 0; }
  html, body {
    width: 869px; height: 1200px; overflow: hidden;
    background: var(--stage);
    font-family: "Poppins", sans-serif;
  }
  .sheet { position: relative; width: 869px; height: 1200px; }

  .exhibit {
    position: absolute; width: 345px; height: 345px;
    background: var(--paper); overflow: hidden;
  }
  .exhibit--a { left: 69px;  top: 54px; }
  .exhibit--b { left: 449px; top: 54px; }
  .exhibit--c { left: 69px;  top: 434px; }
  .exhibit--d { left: 449px; top: 434px; }
  .exhibit--e { left: 262px; top: 811px; }

  .swoosh { position: absolute; inset: 0; width: 345px; height: 345px; }
  .swoosh--mirrored { transform: scaleX(-1); }

  .exhibit-tab {
    position: absolute; top: 25px; height: 42px; width: 226px;
    display: flex; align-items: center; justify-content: center;
    color: var(--paper); font-weight: 600; font-size: 22px; letter-spacing: 2.5px;
  }
  .exhibit-tab--left {
    left: 0; border-radius: 0 21px 21px 0;
    background: linear-gradient(90deg, var(--tab-light), var(--tab-dark) 45%);
  }
  .exhibit-tab--right {
    right: 0; border-radius: 21px 0 0 21px;
    background: linear-gradient(90deg, var(--tab-dark) 55%, var(--tab-light));
  }

  /* Exhibit A */
  .scheme { position: absolute; left: 0; top: 0; width: 345px; height: 345px; }
  .scheme-label { font-family: "Oswald", sans-serif; font-size: 6.5px; fill: var(--navy); text-anchor: middle; }

  /* Exhibit B */
  .trend-gear { position: absolute; left: 122px; top: 125px; width: 180px; height: 180px; }
  .trend-word { font-family: "Oswald", sans-serif; font-weight: 600; font-size: 38px; fill: var(--paper); text-anchor: middle; }

  /* Exhibit C */
  .title-banner {
    position: absolute; left: 0; top: 112px; width: 255px; height: 121px;
    border-radius: 0 14px 14px 0;
    background: linear-gradient(90deg, var(--green) 0%, #2f6a3f 60%, #3a3a3a 100%);
    color: var(--paper); text-align: center;
  }
  .title-banner__name { padding-top: 11px; font-size: 19px; line-height: 22px; font-weight: 400; }
  .title-banner__name strong { font-weight: 700; }
  .title-banner__pillars {
    margin-top: 6px; background: var(--red); height: 20px; line-height: 20px;
    font-size: 11px; font-weight: 500;
  }
  .title-banner__note { margin: 6px 20px 0; font-size: 5.6px; line-height: 7px; }

  .wordmark {
    position: absolute; font-weight: 800; color: var(--green);
    font-size: 19px; line-height: 24px; letter-spacing: 0.3px; white-space: nowrap;
  }
  .exhibit--c .wordmark { left: 55px; top: 270px; }
  .exhibit--d .wordmark { left: 135px; top: 98px; }

  /* Exhibit D */
  .shift-pattern { position: absolute; left: 128px; top: 152px; width: 180px; height: 180px; }
  .shift-label { font-weight: 600; font-size: 11px; fill: var(--ink); text-anchor: middle; }

  /* Exhibit E */
  .detail-line {
    position: absolute; left: 28px; top: 78px;
    font-size: 10.5px; font-weight: 600; color: #555555; white-space: nowrap;
  }
  .detail-line .detail-name { color: var(--green); font-weight: 600; }
  .detail-title {
    position: absolute; left: 28px; top: 96px;
    font-size: 25px; font-weight: 800; color: var(--navy); letter-spacing: 0.5px;
  }
  .gearbox-drawing {
    position: absolute; left: 40px; top: 140px; width: 185px; height: 188px;
    background: linear-gradient(180deg, #f1f1f1, var(--placeholder));
    border-radius: 4px;
  }
  .detail-caption {
    position: absolute; left: 58px; top: 331px;
    font-size: 7px; font-weight: 600; color: var(--ink);
  }
</style>
</head>
<body>
<main class="sheet">

  <!-- Exhibit A: strategy scheme -->
  <section class="exhibit exhibit--a">
    <svg class="swoosh" viewBox="0 0 345 345" aria-hidden="true">
      <path d="M345,160 C325,220 312,290 316,345 L345,345 Z" fill="var(--navy)"/>
      <path d="M318,0 C350,60 350,130 345,160 C325,220 312,290 316,345 L306,345 C300,280 318,200 336,140 C345,90 335,40 304,0 Z" fill="var(--red)"/>
    </svg>
    <div class="exhibit-tab exhibit-tab--left">EXHIBIT (A)</div>
    <svg class="scheme" viewBox="0 0 345 345" aria-label="Strategy scheme: four allocations feeding the index strategy">
      <defs>
        <marker id="arrowhead" viewBox="0 0 10 10" refX="8" refY="5" markerWidth="6" markerHeight="6" orient="auto">
          <path d="M0,0 L10,5 L0,10 Z" fill="var(--steel)"/>
        </marker>
      </defs>
      <g stroke="var(--steel)" stroke-width="3" fill="none">
        <line x1="95" y1="110" x2="175" y2="110"/>
        <line x1="65" y1="140" x2="65" y2="220"/>
        <line x1="205" y1="140" x2="205" y2="220"/>
        <line x1="95" y1="250" x2="175" y2="250"/>
      </g>
      <g stroke="var(--steel)" stroke-width="3" marker-end="url(#arrowhead)">
        <line x1="88" y1="132" x2="108" y2="153"/>
        <line x1="182" y1="132" x2="158" y2="153"/>
        <line x1="88" y1="228" x2="108" y2="201"/>
        <line x1="182" y1="228" x2="158" y2="201"/>
      </g>
      <g class="scheme-node">
        <circle cx="65" cy="110" r="30" fill="var(--steel-light)" stroke="var(--steel)" stroke-width="6"/>
        <circle cx="65" cy="110" r="21" fill="var(--paper)"/>
        <text class="scheme-label" x="65" y="108">REBALANCE</text>
        <text class="scheme-label" x="65" y="116">ANNUALLY</text>
      </g>
      <g class="scheme-node">
        <circle cx="205" cy="110" r="30" fill="var(--steel-light)" stroke="var(--steel)" stroke-width="6"/>
        <circle cx="205" cy="110" r="21" fill="var(--paper)"/>
        <text class="scheme-label" x="205" y="108">TREND 33%</text>
        <text class="scheme-label" x="205" y="116">ALLOCATION</text>
      </g>
      <g class="scheme-node">
        <circle cx="132" cy="177" r="32" fill="var(--steel-light)" stroke="var(--steel)" stroke-width="6"/>
        <circle cx="132" cy="177" r="23" fill="var(--paper)"/>
        <text class="scheme-label" x="132" y="168">5MARBLE</text>
        <text class="scheme-label" x="132" y="176">WORLD STOCK</text>
        <text class="scheme-label" x="132" y="184">INDEX</text>
        <text class="scheme-label" x="132" y="192">STRATEGY</text>
      </g>
      <g class="scheme-node">
        <circle cx="65" cy="250" r="30" fill="var(--steel-light)" stroke="var(--steel)" stroke-width="6"/>
        <circle cx="65" cy="250" r="21" fill="var(--paper)"/>
        <text class="scheme-label" x="65" y="243">BUY &amp; HOLD</text>
        <text class="scheme-label" x="65" y="251">33%</text>
        <text class="scheme-label" x="65" y="259">ALLOCATION</text>
      </g>
      <g class="scheme-node">
        <circle cx="205" cy="250" r="30" fill="var(--steel-light)" stroke="var(--steel)" stroke-width="6"/>
        <circle cx="205" cy="250" r="21" fill="var(--paper)"/>
        <text class="scheme-label" x="205" y="243">TACTICAL</text>
        <text class="scheme-label" x="205" y="251">33%</text>
        <text class="scheme-label" x="205" y="259">ALLOCATION</text>
      </g>
    </svg>
  </section>

  <!-- Exhibit B: trend shift -->
  <section class="exhibit exhibit--b">
    <svg class="swoosh" viewBox="0 0 345 345" aria-hidden="true">
      <path d="M0,30 C20,150 80,280 170,345 L0,345 Z" fill="var(--navy)"/>
      <path d="M8,0 C10,120 70,270 170,345 L150,345 C55,270 -5,150 0,30 L0,0 Z" fill="var(--red)"/>
    </svg>
    <div class="exhibit-tab exhibit-tab--right">EXHIBIT (B)</div>
    <svg class="trend-gear" viewBox="0 0 180 180" aria-label="Trend shift">
      <circle cx="90" cy="90" r="88" fill="var(--green)"/>
      <circle cx="90" cy="90" r="62" fill="var(--paper)"/>
      <circle cx="90" cy="90" r="56" fill="var(--green-deep)"/>
      <text class="trend-word" x="90" y="104">TREND</text>
    </svg>
  </section>

  <!-- Exhibit C: title lockup -->
  <section class="exhibit exhibit--c">
    <svg class="swoosh" viewBox="0 0 345 345" aria-hidden="true">
      <path d="M200,0 L345,0 L345,300 C330,150 290,50 200,0 Z" fill="var(--navy)"/>
      <path d="M180,0 C280,35 332,160 336,345 L345,345 L345,300 C330,150 290,50 200,0 Z" fill="var(--red)"/>
    </svg>
    <div class="exhibit-tab exhibit-tab--left">EXHIBIT (C)</div>
    <div class="title-banner">
      <p class="title-banner__name">5Marble World Stock<br>Index <strong>Strategy</strong></p>
      <p class="title-banner__pillars">Buy &amp; Hold, Trend, Tactical and Rebalance</p>
      <p class="title-banner__note">A multifaceted approach to earning World Equity Returns intended to mitigate drawdowns and replace all or a portion of your equity allocation</p>
    </div>
    <p class="wordmark">5Marble Strategy</p>
  </section>

  <!-- Exhibit D: shift pattern -->
  <section class="exhibit exhibit--d">
    <svg class="swoosh swoosh--mirrored" viewBox="0 0 345 345" aria-hidden="true">
      <path d="M200,0 L345,0 L345,300 C330,150 290,50 200,0 Z" fill="var(--navy)"/>
      <path d="M180,0 C280,35 332,160 336,345 L345,345 L345,300 C330,150 290,50 200,0 Z" fill="var(--red)"/>
    </svg>
    <div class="exhibit-tab exhibit-tab--right">EXHIBIT (D)</div>
    <p class="wordmark">5Marble Strategy</p>
    <svg class="shift-pattern" viewBox="0 0 196 196" aria-label="Three-position shift pattern">
      <circle cx="98" cy="98" r="94" fill="var(--paper)" stroke="var(--red)" stroke-width="2.5"/>
      <g stroke="var(--navy)" stroke-width="6" stroke-linecap="butt">
        <line x1="62" y1="64" x2="62" y2="140"/>
        <line x1="124" y1="64" x2="124" y2="140"/>
        <line x1="62" y1="102" x2="124" y2="102"/>
      </g>
      <text class="shift-label" x="62" y="54">TEXT</text>
      <text class="shift-label" x="124" y="54">TEXT</text>
      <text class="shift-label" x="62" y="158">TEXT</text>
      <circle cx="124" cy="146" r="13" fill="var(--tab-dark)" stroke="var(--steel)" stroke-width="3"/>
      <text x="124" y="148.5" font-family="Oswald, sans-serif" font-size="6" fill="var(--paper)" text-anchor="middle">TREND</text>
    </svg>
  </section>

  <!-- Exhibit E: transmission detail -->
  <section class="exhibit exhibit--e">
    <svg class="swoosh" viewBox="0 0 345 345" aria-hidden="true">
      <path d="M200,0 L345,0 L345,300 C330,150 290,50 200,0 Z" fill="var(--navy)"/>
      <path d="M180,0 C280,35 332,160 336,345 L345,345 L345,300 C330,150 290,50 200,0 Z" fill="var(--red)"/>
    </svg>
    <div class="exhibit-tab exhibit-tab--left">EXHIBIT (E)</div>
    <p class="detail-line">Details of <span class="detail-name">5Marble Strategy</span> Transmission</p>
    <h2 class="detail-title">THE TACTICS</h2>
    <div class="gearbox-drawing" role="img" aria-label="Line drawing of a manual gearbox with shift lever and gears in first speed"></div>
    <p class="detail-caption">First speed engaged</p>
  </section>

</main>
</body>
</html>
```